Sign - Pricing "Menu" Board
Pimble Grove
Project: Sign - Pricing "Menu" Board
Sign - Pricing "Menu" Board  - Children
Creative Brief
This sign will be printed and be placed over desk for all customers to view. It will be in very large print in the front entrance for our new business so provide a quick pricing guide for our services. Our website can be viewed at https://pimblegrove.example.
Children
parents with kids under 7, day cares, pre-schools, grandparents, elementary schools
1. Cohesive feel with website 2. Include all of our services - Drop In Play, Pimble Sparks Programs, Memberships, Kids Night Out, Birthday Parties, Socks - $2 a pair Harriet & Gus Toys - prices vary 3. Our play place will feature home build by Tobby Nook homes. You can use photos from there site if you want. The playhouses can be found in their main street collection - we will feature (market, gas station, dr. office, animal hospital, diner) 4. We are looking for fun quick way for customers to see the pricing when they come in. 5. Everyone will need to sign a waiver to play. That should be included some place on the sign.

```html
<!DOCTYPE html>
<html lang="en">
<head>
<meta charset="utf-8">
<title>Pimble Grove – Pricing Board</title>
<link rel="stylesheet" href="https://fonts.googleapis.com/css2?family=Luckiest+Guy&family=Oswald:wght@500;600&family=Roboto+Condensed:wght@400;700&display=swap">
<style>
  :root{
    --red:#e3202a;
    --blue:#1f58a8;
    --navy:#1c3f7e;
    --text:#2a5aa8;
    --white:#ffffff;
    --photo-a:#c9b39a;
    --photo-b:#9c8a76;
  }
  *{box-sizing:border-box;margin:0;padding:0}
  html,body{width:1200px;height:901px;overflow:hidden;background:var(--white)}
  body{position:relative;font-family:"Roboto Condensed",Arial,sans-serif;color:var(--text)}
  .board{position:absolute;left:0;top:110px;width:1200px;height:693px;overflow:hidden;background:var(--white)}
  .hero-photo{position:absolute;left:0;top:0;width:300px;height:470px;background:radial-gradient(ellipse at 40% 40%,var(--photo-a),var(--photo-b) 75%,#e8e4df 100%)}
  .header-band{position:absolute;left:0;top:0;width:1200px;height:125px}
  .headline{position:absolute;left:262px;top:22px;width:900px;text-align:center;font-family:"Luckiest Guy",Impact,sans-serif;font-size:58px;color:var(--white);letter-spacing:1px}
  .section-tab{position:absolute;height:38px;display:flex;align-items:center}
  .section-tab svg.star{width:30px;height:30px;margin-right:6px}
  .section-tab .tab{height:38px;line-height:38px;padding:0 30px 0 14px;background:var(--blue);color:var(--white);font-family:"Oswald",Arial,sans-serif;font-weight:600;font-size:27px;clip-path:polygon(0 0,100% 0,88% 100%,0 100%);border-radius:8px 0 0 8px}
  .price-list{position:absolute;list-style:none}
  .price-row{display:flex;align-items:baseline;font-size:19px;line-height:26px;color:var(--text)}
  .price-row .leader{flex:1;border-bottom:2px dotted var(--text);margin:0 4px;transform:translateY(-4px)}
  .price-row .amount{font-weight:700;color:var(--navy)}
  .price-row small{font-size:11px}
  .fine-print{font-size:11px;line-height:14px;color:var(--navy)}
  .day-label{font-weight:700;color:var(--red);font-size:19px;line-height:27px}
  .notice{position:absolute;left:29px;top:430px;width:214px;height:207px;background:var(--white);border:4px solid var(--red);text-align:center;padding:14px 10px}
  .notice-title{display:flex;align-items:center;justify-content:center;gap:6px;font-weight:700;font-size:21px;color:var(--blue)}
  .notice-title .dot{width:24px;height:24px;border-radius:50%;background:var(--blue);color:var(--white);font-size:18px;line-height:24px}
  .notice p{color:var(--red);font-size:19px;line-height:24px;margin-top:8px}
  .notice hr{border:0;border-top:2px solid var(--red);margin:8px 6px 0}
  .socks-sign{position:absolute;left:1012px;top:396px;width:158px;height:48px;background:var(--red);color:var(--white);font-family:"Oswald",Arial,sans-serif;font-weight:600;font-size:26px;line-height:48px;text-align:center;border-radius:4px}
  .socks-post{position:absolute;left:1086px;top:444px;width:10px;height:70px;background:var(--blue)}
  .playhouse-art{position:absolute;left:960px;top:505px;width:232px;height:165px;background:linear-gradient(180deg,#f3f6fb,#c9d6ec);border-radius:6px}
  .waves{position:absolute;left:0;top:600px;width:1200px;height:93px}
</style>
</head>
<body>
<main class="board">
  <div class="hero-photo" role="img" aria-label="Photo of a smiling young child at the play centre"></div>

  <svg class="header-band" viewBox="0 0 1200 125" preserveAspectRatio="none" aria-hidden="true">
    <path d="M300 0 H1200 V92 Q760 128 255 104 Q268 40 300 0 Z" fill="var(--red)"/>
  </svg>
  <h1 class="headline">Where Imagination Happens</h1>

  <!-- Left column -->
  <div class="section-tab" style="left:258px;top:127px">
    <svg class="star" viewBox="0 0 24 24"><path d="M12 1l3.2 7 7.6.7-5.8 5 1.8 7.5L12 17.3 5.2 21.2 7 13.7 1.2 8.7l7.6-.7z" fill="var(--red)"/></svg>
    <span class="tab">Drop in Play</span>
  </div>
  <ul class="price-list" style="left:287px;top:172px;width:330px">
    <li class="price-row"><span>Single Child</span><span class="leader"></span><span class="amount">$12</span></li>
    <li class="price-row"><span>Each Additional Child</span><span class="leader"></span><span class="amount">$10</span></li>
    <li class="fine-print">Covers all day play including reentry on the same calendar day</li>
  </ul>

  <div class="section-tab" style="left:258px;top:253px">
    <svg class="star" viewBox="0 0 24 24"><path d="M12 1l3.2 7 7.6.7-5.8 5 1.8 7.5L12 17.3 5.2 21.2 7 13.7 1.2 8.7l7.6-.7z" fill="var(--red)"/></svg>
    <span class="tab">Kids Night Out</span>
  </div>
  <ul class="price-list" style="left:287px;top:294px;width:330px">
    <li class="day-label">Every Thursday Night 5pm - 8pm</li>
    <li class="price-row"><span>Single Child</span><span class="leader"></span><span class="amount">$25</span></li>
    <li class="price-row"><span>Each Additional Child</span><span class="leader"></span><span class="amount">$20</span></li>
  </ul>

  <div class="section-tab" style="left:258px;top:380px">
    <svg class="star" viewBox="0 0 24 24"><path d="M12 1l3.2 7 7.6.7-5.8 5 1.8 7.5L12 17.3 5.2 21.2 7 13.7 1.2 8.7l7.6-.7z" fill="var(--red)"/></svg>
    <span class="tab">Birthday Parties</span>
  </div>
  <ul class="price-list" style="left:287px;top:422px;width:330px">
    <li class="day-label">Weekdays</li>
    <li class="price-row"><span>Main Floor Garden Party</span><span class="leader"></span><span class="amount">$150</span></li>
    <li class="price-row"><span>Mezzanine Tree Top Party</span><span class="leader"></span><span class="amount">$175</span></li>
    <li class="day-label">Weekends</li>
    <li class="price-row"><span>Main Floor Garden Party</span><span class="leader"></span><span class="amount">$250</span></li>
    <li class="price-row"><span>Mezzanine Tree Top Party</span><span class="leader"></span><span class="amount">$275</span></li>
    <li class="price-row"><span>Busy Bee Party <small>(Any Day of the Week)</small></span><span class="leader"></span><span class="amount">$650</span></li>
  </ul>

  <aside class="notice">
    <div class="notice-title"><span class="dot">!</span>Please Note:</div>
    <p>Everyone needs to sign a waiver to play</p>
    <hr>
    <p>Children must be supervised at all times</p>
  </aside>

  <!-- Right column -->
  <div class="section-tab" style="left:640px;top:127px">
    <svg class="star" viewBox="0 0 24 24"><path d="M12 1l3.2 7 7.6.7-5.8 5 1.8 7.5L12 17.3 5.2 21.2 7 13.7 1.2 8.7l7.6-.7z" fill="var(--red)"/></svg>
    <span class="tab">School Field Trips</span>
  </div>
  <ul class="price-list" style="left:677px;top:172px;width:232px">
    <li class="price-row"><span>Per Child</span><span class="leader"></span><span class="amount">$5</span></li>
    <li class="price-row"><span>Adults</span><span class="leader"></span><span class="amount">Free</span></li>
    <li class="fine-print" style="margin-top:2px">Open for field trips Monday 7am to 4pm<br>Recommended for children 3-7 years old<br>Minimum of 10 participants</li>
  </ul>

  <div class="section-tab" style="left:640px;top:282px">
    <svg class="star" viewBox="0 0 24 24"><path d="M12 1l3.2 7 7.6.7-5.8 5 1.8 7.5L12 17.3 5.2 21.2 7 13.7 1.2 8.7l7.6-.7z" fill="var(--red)"/></svg>
    <span class="tab">Pimble Sparks Programs</span>
  </div>
  <div class="price-list" style="left:677px;top:324px;width:400px">
    <div style="display:flex;justify-content:space-between">
      <div class="day-label">Tuesday, Wednesday, Thursday,<br>and Friday</div>
      <div style="text-align:center;font-weight:700;color:var(--navy);font-size:19px;line-height:27px">$2 (Per Class)<div class="fine-print">(Plus Regular Admission)</div></div>
    </div>
    <div class="fine-print" style="margin-top:2px">First Class 10am - 11am<br>Second Class 4pm - 5pm</div>
  </div>

  <div class="section-tab" style="left:640px;top:426px">
    <svg class="star" viewBox="0 0 24 24"><path d="M12 1l3.2 7 7.6.7-5.8 5 1.8 7.5L12 17.3 5.2 21.2 7 13.7 1.2 8.7l7.6-.7z" fill="var(--red)"/></svg>
    <span class="tab">Memberships</span>
  </div>
  <ul class="price-list" style="left:677px;top:462px;width:272px">
    <li class="price-row"><span>1 Child Monthly Membership</span><span class="leader"></span><span class="amount">$30</span></li>
    <li class="price-row"><span>2+ Children Monthly Membership</span><span class="leader"></span><span class="amount">$45</span></li>
    <li class="fine-print">Include all of the daily Pimble Sparks programs and a 15% discount for any birthday party package</li>
  </ul>

  <div class="socks-post"></div>
  <div class="socks-sign">Socks $2.00</div>
  <div class="playhouse-art" role="img" aria-label="Illustration of a blue playhouse with two cartoon children"></div>

  <svg class="waves" viewBox="0 0 1200 93" preserveAspectRatio="none" aria-hidden="true">
    <path d="M0 40 Q150 10 300 40 T600 40 T900 40 T1200 40 V93 H0 Z" fill="var(--red)"/>
    <path d="M0 58 Q150 30 300 58 T600 58 T900 58 T1200 58 V93 H0 Z" fill="var(--white)"/>
    <path d="M0 70 Q150 46 300 70 T600 70 T900 70 T1200 70 V93 H0 Z" fill="var(--blue)"/>
  </svg>
</main>
</body>
</html>
```